TALBRIDGE ELEVATOR CORP

LOOKING FOR BLACK MATTE BACKGROUND WITH GLOSS DESIGN
NEED RAISED UV ON LOGO AND LETTERING , WITH ROUNDED CORNERS AND COLORED EDGES ( FLOURECENT BLUE)

```html
<!DOCTYPE html>
<html lang="en">
<head>
<meta charset="utf-8">
<title>Talbridge Elevator Corp – Business Cards</title>
<link href="https://fonts.googleapis.com/css2?family=Lato:wght@400;700;900&family=EB+Garamond:wght@400;500&display=swap" rel="stylesheet">
<style>
  :root{
    --bg:#5c5c5c;
    --card-dark:#2b2a2b;
    --card-white:#ffffff;
    --ink:#1d1d1d;
    --text:#333333;
    --blue:#2a5fb0;
    --green:#3a9a3a;
    --silver:#c9c9c9;
    --matte-line:#3a393a;
  }
  *{margin:0;padding:0;box-sizing:border-box}
  html,body{width:1200px;height:900px;overflow:hidden}
  body{background:var(--bg);position:relative;font-family:"Lato",sans-serif}

  .card{position:absolute;width:520px;height:300px;border-radius:16px;overflow:hidden;
    box-shadow:0 0 0 3px var(--blue)}
  .card--front{left:50px;top:300px;background:var(--card-white)}
  .card--back{left:630px;top:300px;background:var(--card-dark)}

  .front-wave{position:absolute;inset:0;width:100%;height:100%}

  .brand{position:absolute;left:42px;top:48px;display:flex;align-items:center;gap:12px}
  .brand__dot{width:58px;height:58px;border-radius:50%;background:var(--blue);flex:none}
  .brand__name{font-weight:900;font-size:15px;line-height:1.05;color:var(--ink);letter-spacing:.5px;text-transform:uppercase}

  .divider{position:absolute;left:232px;top:40px;width:1.5px;height:150px;background:var(--blue)}

  .contact{position:absolute;left:252px;top:40px;color:var(--text)}
  .contact__name{font-weight:900;font-size:28px;letter-spacing:.5px;line-height:1}
  .contact__first{color:var(--blue)}
  .contact__last{color:var(--green)}
  .contact__role{font-size:12.5px;margin-top:6px;line-height:1.3}
  .contact__address{font-size:12.5px;margin-top:8px;line-height:1.3}
  .contact__row{display:flex;align-items:center;gap:7px;font-size:12.5px;margin-top:3px}
  .contact__row svg{width:11px;height:11px;flex:none}
  .contact__row:first-of-type{margin-top:4px}

  .back-grain{position:absolute;inset:0;background:repeating-linear-gradient(180deg,transparent 0 44px,var(--matte-line) 44px 46px);opacity:.5}
  .back-brand{position:absolute;left:0;right:0;top:62px;display:flex;flex-direction:column;align-items:center}
  .back-brand__dot{width:96px;height:96px;border-radius:50%;background:var(--blue)}
  .back-brand__title{margin-top:20px;display:flex;align-items:center;gap:16px;font-family:"EB Garamond",serif;
    font-size:25px;color:var(--silver);letter-spacing:1.5px;text-transform:uppercase}
  .back-brand__rule{width:52px;height:2px;background:var(--silver)}
  .back-brand__tagline{margin-top:4px;font-family:"EB Garamond",serif;font-size:15px;color:var(--silver);letter-spacing:2px;text-transform:uppercase}
</style>
</head>
<body>

<section class="card card--front" aria-label="Business card front">
  <svg class="front-wave" viewBox="0 0 520 300" preserveAspectRatio="none" aria-hidden="true">
    <path d="M0,78 C120,150 300,240 520,296 L520,300 L0,300 Z" fill="var(--card-dark)"/>
    <path d="M80,128 C220,200 360,258 520,288" fill="none" stroke="var(--blue)" stroke-width="5"/>
    <path d="M92,124 C230,194 370,250 520,280" fill="none" stroke="var(--green)" stroke-width="4"/>
  </svg>

  <div class="brand">
    <span class="brand__dot"></span>
    <span class="brand__name">Talbridge<br>Elevator<br>Corp</span>
  </div>

  <div class="divider"></div>

  <div class="contact">
    <h1 class="contact__name"><span class="contact__first">DANIEL</span> <span class="contact__last">HARLOW</span></h1>
    <p class="contact__role">President<br>Talbridge Elevator Corp</p>
    <p class="contact__address">2271 Harrow Ridge Avenue,<br>Bronx, NY 10465</p>
    <p class="contact__row">
      <svg viewBox="0 0 24 24"><path fill="var(--blue)" d="M6.6 10.8a15 15 0 0 0 6.6 6.6l2.2-2.2c.3-.3.7-.4 1-.2 1.1.4 2.3.6 3.6.6.6 0 1 .4 1 1V20c0 .6-.4 1-1 1A17 17 0 0 1 3 4c0-.6.4-1 1-1h3.5c.6 0 1 .4 1 1 0 1.3.2 2.5.6 3.6.1.3 0 .7-.2 1z"/></svg>
      555-204-7781
    </p>
    <p class="contact__row">
      <svg viewBox="0 0 24 24"><rect x="2" y="5" width="20" height="14" rx="1" fill="var(--blue)"/><path d="M2 6l10 7 10-7" fill="none" stroke="#fff" stroke-width="2"/></svg>
      talbridgelift@mail.com
    </p>
    <p class="contact__row">
      <svg viewBox="0 0 24 24"><circle cx="12" cy="12" r="10" fill="var(--blue)"/><path d="M2 12h20M12 2c3 3 3 17 0 20M12 2c-3 3-3 17 0 20" fill="none" stroke="#fff" stroke-width="1.5"/></svg>
      www.talbridgeelevatorny.com
    </p>
  </div>
</section>

<section class="card card--back" aria-label="Business card back">
  <div class="back-grain"></div>
  <div class="back-brand">
    <span class="back-brand__dot"></span>
    <div class="back-brand__title">
      <span class="back-brand__rule"></span>
      <span>Talbridge Elevator Corp</span>
      <span class="back-brand__rule"></span>
    </div>
    <p class="back-brand__tagline">Elevator Services</p>
  </div>
</section>

</body>
</html>
```